Patty Cove Business Card/Logo/Stationary (Restaurant)

Please check out our instagram (@pattycove) for inspiration.

This project is for a NEW design... examples below are just for reference. Please do not submit the images below on a card.

We're a New Zealand inspired gastropub serving award-winning gourmet burgers. Our restaurant is called Patty Cove! A Bach is a New Zealand term for a ‘holiday home’ where family and friends choose to vacation. Baches are an extensive part of New Zealand’s culture and were thought to be originally short for bachelor pad, but actually tended to be a family holiday home.

We've had the same bland business card design for years and want something new and updated. We'd like to see something that is very eye-catching that sets us apart from your average run-of-the-mill business card.

We serve three communities with five locations in - Richmond, VA; Charlottesville, VA; and Durham, NC.

Industry/Entity Type

Burger Restaurant

Contact Information for Business Card

One side for a name, email, phone number and title but still POPS... The other side eye catching and unique.

Colors

Designer to choose colors to be used in the design.

Requirements
Nice to have
• We like these sayings:
• "A New Zealand Inspired Gastropub"
• "Life's a Cove"
• "All Green No Grain"
• "Life's Better at the Cove"
• "Intelligent Indulgence"
Should not have
• We are an upscale dine-in burger concept and not a typical dive bar or burger joint. We do not want to see "diner style" logos and designs.

```html
<!DOCTYPE html>
<html lang="en">
<head>
<meta charset="utf-8">
<title>Patty Cove — Business Card</title>
<link rel="stylesheet" href="https://fonts.googleapis.com/css2?family=Oswald:wght@500&family=Josefin+Sans:wght@400;600&display=swap">
<style>
  :root {
    --backdrop: #1c1d1c;
    --card-white: #eef0f3;
    --card-black: #1f2021;
    --band: #252627;
    --band-edge: #3a3b3c;
    --ink: #222324;
    --paper-text: #f2f2f2;
    --rule: #c9cbcd;
    --muted: #bfc1c3;
    --gold: #c7ab78;
  }
  * { margin: 0; padding: 0; box-sizing: border-box; }
  html, body { width: 1200px; height: 800px; overflow: hidden; background: var(--backdrop); }
  .canvas {
    width: 1200px; height: 800px;
    display: flex; align-items: center; justify-content: center; gap: 60px;
  }
  .card {
    width: 525px; height: 300px; position: relative; overflow: hidden;
    box-shadow: 0 10px 30px rgba(0,0,0,.5);
  }

  /* Front side */
  .card--front { background: var(--card-white); }
  .front-header {
    position: absolute; left: 0; right: 0; top: 34px;
    display: flex; flex-direction: column; align-items: center;
  }
  .brand-name {
    font-family: "Oswald", sans-serif; font-weight: 500; font-size: 50px;
    letter-spacing: 4px; line-height: 1; color: var(--ink); text-transform: uppercase;
  }
  .brand-tagline {
    font-family: "Josefin Sans", sans-serif; font-weight: 600; font-size: 14px;
    letter-spacing: .6px; color: var(--ink); margin-top: 6px;
  }
  .contact-band {
    position: absolute; left: 0; right: 0; top: 126px; height: 138px;
    background: var(--band); border-top: 3px solid var(--band-edge);
    display: flex; flex-direction: column; align-items: center; padding-top: 18px;
    color: var(--paper-text); font-family: "Josefin Sans", sans-serif;
  }
  .phone { font-size: 26px; letter-spacing: 2px; font-weight: 400; line-height: 1; }
  .divider { width: 400px; height: 12px; margin: 8px 0 10px; }
  .address { font-size: 13px; letter-spacing: 1.2px; text-transform: uppercase; }
  .email { font-size: 13px; letter-spacing: 1px; color: var(--muted); margin-top: 9px; }

  /* Back side */
  .card--back {
    background: radial-gradient(ellipse at 45% 40%, #2b2c2d 0%, var(--card-black) 72%);
    display: flex; flex-direction: column; align-items: center; justify-content: center;
  }
  .back-mark { display: flex; align-items: center; gap: 16px; }
  .back-mark .mark-dot {
    width: 22px; height: 22px; border-radius: 50%; background: var(--gold);
  }
  .back-name {
    font-family: "Oswald", sans-serif; font-weight: 500; font-size: 56px;
    letter-spacing: 4px; color: var(--paper-text); text-transform: uppercase; line-height: 1;
  }
  .back-rule { width: 250px; height: 2px; background: var(--gold); margin-top: 14px; }
  .back-tagline {
    font-family: "Josefin Sans", sans-serif; font-weight: 600; font-size: 14px;
    color: var(--paper-text); margin-top: 12px; letter-spacing: .6px;
  }
</style>
</head>
<body>
<main class="canvas">
  <section class="card card--front">
    <header class="front-header">
      <h1 class="brand-name">Patty Cove</h1>
      <p class="brand-tagline">A New Zealand Inspired Gastro Pub</p>
    </header>
    <div class="contact-band">
      <p class="phone">555 - 014 - 2210</p>
      <svg class="divider" viewBox="0 0 400 12" aria-hidden="true">
        <line x1="0" y1="6" x2="186" y2="6" stroke="#c9cbcd" stroke-width="1.5"/>
        <path d="M192 6 L196 2 L200 6 L196 10 Z M200 6 L204 2 L208 6 L204 10 Z" fill="#c9cbcd"/>
        <line x1="214" y1="6" x2="400" y2="6" stroke="#c9cbcd" stroke-width="1.5"/>
      </svg>
      <p class="address">48 Harbor Lane Road Bayhaven, VA 20000</p>
      <p class="email">bayhaven@pattycove.com</p>
    </div>
  </section>

  <section class="card card--back">
    <div class="back-mark" role="img" aria-label="Patty Cove logo">
      <span class="mark-dot"></span>
      <span class="back-name">Patty Cove</span>
    </div>
    <span class="back-rule"></span>
    <p class="back-tagline">A New Zealand Inspired Gastro Pub</p>
  </section>
</main>
</body>
</html>
```